Website transfer and revamp for consultancy

We are a professional management consultancy and need our current website transferred and modernised from Wix to WordPress with the most efficient SEO updates and blog included. We are open for options of new site set up.

Website must be relatively easy for us to maintain and update ourselves.

Website must also be desktop/mobile/ipad friendly.

www.tellvane-advisory.com

Target Market(s)

General manufacturers, construction, developers, oil and gas

Industry/Entity Type

Management Consulting

Font styles to use
Serif

Colors

Designer to choose colors to be used in the design.

Requirements
Must have
• Must have same bulk content as the existing website as a minimum with the addition of a blog page. We are open to added content.
Nice to have
• Open to designer additions such as "projects completed" and "value created" number generators
Should not have
• DO NOT USE stock photos which are not free for use to use.

```html
<!DOCTYPE html>
<html lang="en">
<head>
<meta charset="utf-8">
<title>Tellvane Advisory — Management Consultancy</title>
<link href="https://fonts.googleapis.com/css2?family=PT+Serif:wght@400;700&family=Open+Sans:wght@400;600;700&display=swap" rel="stylesheet">
<style>
:root{
  --red:#c41e2e;
  --red-dark:#9e1522;
  --navy:#1d2838;
  --ink:#333b45;
  --muted:#7d8590;
  --light:#f0f0f0;
  --lighter:#f7f7f7;
  --white:#ffffff;
}
*{box-sizing:border-box;margin:0;padding:0}
html,body{width:1200px;height:3196px;overflow:hidden}
body{background:var(--white);font-family:"Open Sans",Arial,sans-serif;color:var(--ink);position:relative}
.serif{font-family:"PT Serif",Georgia,serif}

/* header */
.site-header{height:112px;position:relative}
.brand{position:absolute;left:60px;top:26px;display:flex;align-items:center;gap:14px}
.brand-square{width:40px;height:40px;background:var(--red)}
.brand-name{font-family:"PT Serif",Georgia,serif;font-size:34px;color:var(--navy);line-height:1}
.brand-tag{position:absolute;left:114px;top:72px;font-size:11px;color:var(--muted);letter-spacing:1px}
.header-tools{position:absolute;right:70px;top:50px;display:flex;align-items:center;gap:36px}
.lang{width:80px;height:26px;border:1px solid #ddd;font-size:12px;color:var(--muted);padding:4px 8px}

/* nav */
.main-nav{height:68px;background:var(--red);display:flex;justify-content:center}
.main-nav a{display:flex;align-items:center;padding:0 36px;color:var(--white);text-decoration:none;font-size:15px;font-weight:600;letter-spacing:.5px}
.main-nav a.active{background:var(--navy);}

/* hero */
.hero{height:580px;background:linear-gradient(180deg,#7f93a6 0%,#c7d1da 55%,#ffffff 100%)}

/* welcome */
.welcome{height:440px;text-align:center;padding-top:60px}
.section-title{font-family:"PT Serif",Georgia,serif;color:var(--red);font-size:48px;font-weight:400;letter-spacing:1px}
.welcome p{width:860px;margin:18px auto 0;font-size:13px;line-height:1.7;color:var(--muted)}
.btn{display:inline-block;background:var(--navy);color:var(--white);font-size:14px;font-weight:600;padding:14px 30px;letter-spacing:.5px;text-decoration:none}
.welcome .btn{margin-top:40px}

/* why */
.why{height:410px;position:relative;background:linear-gradient(90deg,#1a2230 0%,#2f3a48 45%,#6a6f75 100%)}
.why-inner{position:absolute;left:70px;top:80px;width:520px;color:var(--white)}
.why h2{font-family:"PT Serif",Georgia,serif;font-size:50px;font-weight:400}
.why p{font-size:13px;line-height:1.7;margin-top:16px;color:#dfe3e8}
.why .btn{background:var(--white);color:var(--navy);margin-top:36px}
.dots{position:absolute;left:570px;bottom:18px;display:flex;gap:8px}
.dots span{width:9px;height:9px;border-radius:50%;background:#aaa}
.dots span.on{background:var(--white)}

/* services */
.services{height:570px;display:flex}
.service{flex:1;text-align:center;padding-top:70px}
.service.conflict{background:var(--light)}
.service.contract{background:var(--lighter)}
.service-icon{width:150px;height:120px;margin:0 auto;border-radius:6px}
.service h3{font-family:"PT Serif",Georgia,serif;color:var(--red);font-size:42px;font-weight:400;margin-top:30px}
.service p{width:440px;margin:20px auto 0;font-size:13px;line-height:1.7;color:var(--muted)}
.service .btn{margin-top:36px}

/* testimonial */
.testimonial{height:400px;text-align:center;padding-top:70px}
.quote{width:820px;margin:40px auto 0;border:1px solid #e3e3e3;padding:22px 40px;font-size:13px;line-height:1.7;color:var(--muted)}
.client{display:flex;align-items:center;justify-content:center;gap:20px;margin-top:40px}
.avatar{width:72px;height:72px;border-radius:50%;background:#c9cfd6}
.client-name{font-family:"PT Serif",Georgia,serif;font-size:24px;color:var(--ink)}
.client-role{font-size:12px;color:var(--muted);margin-left:8px}

/* projects */
.projects{height:380px;display:grid;grid-template-columns:repeat(4,300px);grid-template-rows:190px 190px}
.project{padding:28px 40px;color:var(--white)}
.project.red{background:var(--red)}
.project.plain{background:var(--white);color:var(--ink)}
.project h4{font-family:"PT Serif",Georgia,serif;font-size:28px;font-weight:700}
.project p{font-size:13px;line-height:1.6;margin-top:12px}
.photo.tree{background:linear-gradient(160deg,#6b6150,#3d3a33)}
.photo.laptop{background:linear-gradient(160deg,#2a2f36,#596370)}
.photo.plant{background:linear-gradient(160deg,#8a6b45,#4f6a2e)}
.photo.team{background:linear-gradient(160deg,#9a8b7a,#4b4c52)}

/* footer */
.site-footer{height:200px;display:flex;padding:42px 60px 0;gap:0}
.foot-col{width:270px}
.foot-col h5{font-family:"PT Serif",Georgia,serif;font-size:20px;color:var(--navy);font-weight:700;letter-spacing:1px}
.foot-col p{font-size:13px;color:var(--muted);margin-top:18px;line-height:1.6}
.social{display:flex;gap:18px;margin-top:20px}
.social span{width:18px;height:18px;border-radius:50%;background:var(--navy)}
.bottom-bar{height:36px;background:var(--red);color:var(--white);font-size:12px;display:flex;align-items:center;justify-content:center}
</style>
</head>
<body>

<header class="site-header">
  <div class="brand"><span class="brand-square"></span><span class="brand-name">Tellvane Advisory</span></div>
  <div class="brand-tag">MANAGEMENT CONSULTANCY</div>
  <div class="header-tools">
    <svg width="20" height="20" viewBox="0 0 20 20" aria-label="Search"><circle cx="8" cy="8" r="6" fill="none" stroke="#1d2838" stroke-width="2"/><line x1="12.5" y1="12.5" x2="18" y2="18" stroke="#1d2838" stroke-width="2"/></svg>
    <div class="lang">English ▾</div>
  </div>
</header>

<nav class="main-nav">
  <a class="active" href="#">HOME</a>
  <a href="#">ABOUT US</a>
  <a href="#">SERVICES</a>
  <a href="#">BROCHURE</a>
  <a href="#">ARTICLE</a>
  <a href="#">CONTACT US</a>
</nav>

<section class="hero" role="img" aria-label="Laptop on a desk in front of a city skyline with floating words about business strategy and ideas"></section>

<section class="welcome">
  <h1 class="section-title">WELCOME TO TELLVANE ADVISORY</h1>
  <p>Observing the magnitude of contractual engagements and conflicts, we believe we can make things better: better engagement, better outcomes, better performance, which all lead to better value in terms of financial benefit and relationship maintenance.</p>
  <p>Observing the magnitude of contractual engagements and conflicts, we believe we can make things better: better engagement, better outcomes, better performance, which all lead to better value in terms of financial benefit and relationship maintenance.</p>
  <a class="btn" href="#">READ MORE</a>
</section>

<section class="why" role="img" aria-label="Team of consultants working together around a laptop in a dim office">
  <div class="why-inner">
    <h2>WHY CHOOSE US?</h2>
    <p>Observing the magnitude of contractual engagements and conflicts, we see opportunity to make things better: better performance, which ultimately leads to better value in terms of financial benefit and relationship maintenance.</p>
    <a class="btn" href="#">READ MORE</a>
  </div>
  <div class="dots"><span class="on"></span><span></span><span></span></div>
</section>

<section class="services">
  <div class="service conflict">
    <div class="service-icon" role="img" aria-label="Illustration of people meeting around a table" style="background:#dcdcdc"></div>
    <h3>Conflict Advisory</h3>
    <p>In any conflict we step in early, as in the promise we deliver effective solutions to contractual and commercial disputes with the aim of reducing time, cost, relationships and strengthening the parties for the future ahead.</p>
    <a class="btn" href="#">READ MORE</a>
  </div>
  <div class="service contract">
    <div class="service-icon" role="img" aria-label="Illustration of contract documents" style="background:#e2e2e2"></div>
    <h3>Contract Advisory</h3>
    <p>Effective contract management delivered through our contract advisors ensures that the contract is as effective as it can be. Through proper planning and effective application, we ensure that contractual disruptions are minimised and risks are mitigated through the full contract life cycle.</p>
    <a class="btn" href="#">READ MORE</a>
  </div>
</section>

<section class="testimonial">
  <h2 class="section-title">CLIENT SAY ABOUT US</h2>
  <div class="quote">"Lorem Ipsum is simply dummy text of the printing and typesetting industry. Lorem Ipsum has been the industry's standard dummy text ever since the 1500s, when an unknown printer took a galley of type and scrambled it to make a type specimen book."</div>
  <div class="client">
    <div class="avatar" role="img" aria-label="Client portrait"></div>
    <div><span class="client-name">Lorem ipsum,</span><span class="client-role">CEO of Company Name</span></div>
  </div>
</section>

<section class="projects">
  <div class="project red"><h4>Project Name</h4><p>"Lorem Ipsum is simply dummy text of the printing and typesetting industry.</p></div>
  <div class="photo tree" role="img" aria-label="Bare tree in warm light"></div>
  <div class="project red"><h4>Project Name</h4><p>"Lorem Ipsum is simply dummy text of the printing and typesetting industry.</p></div>
  <div class="photo laptop" role="img" aria-label="Laptop on a dark desk"></div>
  <div class="photo plant" role="img" aria-label="Hands holding a young plant in soil"></div>
  <div class="project plain"><h4>Project Name</h4><p>"Lorem Ipsum is simply dummy text of the printing and typesetting industry.</p></div>
  <div class="photo team" role="img" aria-label="Colleagues working together at a table"></div>
  <div class="project red"><h4>Project Name</h4><p>"Lorem Ipsum is simply dummy text of the printing and typesetting industry.</p></div>
</section>

<footer class="site-footer">
  <div class="foot-col"><h5>SAY HELLO:</h5><p>info@tellvane-advisory.com</p></div>
  <div class="foot-col"><h5>GIVE US A RING:</h5><p>+44 (0)20 5550 1847</p></div>
  <div class="foot-col"><h5>MAKE A VISIT:</h5><p>2nd Floor, Harrow Court,<br>18 Quayside Lane,<br>Mercer Square, Dunmoor</p></div>
  <div class="foot-col"><h5>KEEP UP:</h5><div class="social"><span></span><span></span></div></div>
</footer>
<div class="bottom-bar">© Tellvane Advisory Limited · 2017. All Rights Reserved</div>

</body>
</html>
```